QLM book cover for The Harbor Ledger SELF HELP BOOK

I need a book cover for my book The Harbor Ledger. It needs to catch your attention and even though I dont see how you can use faces in a blueprint image, I do like how they catch your eye. so maybe 2 images of people they can be unisex images in a blueprint format with my title and subtitle and my name and the spine and the back all ready to make a QLM book cover. I see it as a blue theme with white blueprint imagery and also a commitment theme. Here are the details from QLM: File Format and Structure

Format: Single PDF file (preferred for print). QLM converts other formats (e.g., DOCX) but PDF ensures accuracy.
Structure: One continuous image including:
Back cover (with space for barcode if not provided by QLM).
Spine (text/logo if ≥79 pages; otherwise, leave blank).
Front cover.

No Separate Files: Everything must be in one flattened PDF—no layers or editable elements.
Barcode: Leave a white 2x1.2-inch (5x3 cm) space on the back cover (bottom right). QLM adds it automatically unless you provide your own (upload as a separate image).

2. Color Mode and Profiles

Color Space: RGB (Red-Green-Blue). QLM does not support CMYK (Cyan-Magenta-Yellow-Black) for print-on-demand, as it uses digital inkjet/toner printers optimized for RGB.
No Color Profiles: Do not embed ICC profiles (e.g., sRGB)—they're automatically removed and can cause unexpected shifts.
No Spot Colors: Avoid Chromel or specialty inks; they're incompatible with QLM's process.
Color Variance Tip: Expect slight shifts due to printer differences. Test with a proof copy. For best results, design in sRGB and preview in Vexor Pagely.

3. Resolution and Image Quality

DPI (Dots Per Inch): Minimum 300 DPI at final print size. Lower resolution causes pixelation or rejection.
File Size: Up to 650 MB, but aim for under 50 MB for faster uploads.
Compression: Use JPEG or TIFF for images within the PDF; avoid heavy compression that degrades quality.

4. Dimensions and Bleed

Total Width Calculation: Back cover width + Spine width + Front cover width + Bleed (0.125 inches/3.2 mm on all sides).
Front/Back: Matches your trim size (e.g., 6x9 inches = 6" width each).
Spine: Calculated via QLM's tool (depends on page count, ink type, and paper; e.g., 0.066" for a 100-page premium color book).

Height: Trim height + 0.25" (6.4 mm) total bleed (0.125" top + 0.125" bottom).
Example for 6x9" Trim (Common Size):ComponentWidthHeightFront Cover6"9"Back Cover6"9"Spine (varies)~0.06–0.5"9"Total Cover (w/ Bleed)~12.25–13"9.25"
Bleed: Essential for full-bleed designs (e.g., backgrounds extending to edges). Extend artwork 0.125" beyond trim lines; safe text/logo must be 0.125" inside trim.
Trim Sizes: Standard options like 5x8", 6x9", 8.5x11". Custom sizes allowed (4–8.5" wide, 6–11.69" tall), but check page count limits (24–828 pages for premium color).

5. Content and Design Guidelines

Safe Zone: Keep critical elements (text, logos) at least 0.125" from edges to avoid trimming errors.
Spine Text: Centered, readable font (≥8 pt); runs vertically (bottom-to-top for LTR languages). Minimum 79 pages required.
Finish: Glossy (shiny, vibrant) or matte (subtle, non-reflective). Glossy enhances colors but shows fingerprints.
Avoid: Borders that could crop, low-contrast text, or designs assuming offset printing quality.

back cover text:
What if the strength of your relationship came down to one thing—clarity?
Most couples love each other deeply… but still misunderstand each other.
Not because they’re incompatible—because they never built a shared blueprint.

The Harbor Ledger is a transformative relationship workbook designed to help couples replace confusion with clarity, resentment with understanding, and disconnection with deep, lasting partnership.

Inside, you’ll learn how to:

✓ Communicate in ways that build connection—not conflict
✓ Understand each other’s emotional needs, stress responses, and love patterns
✓ Set healthy boundaries without creating distance
✓ Rebuild trust and strengthen loyalty
✓ Navigate gender differences with empathy and confidence
✓ Balance intimacy, time, roles, finances, and expectations
✓ Create agreements that eliminate guesswork and prevent future conflict
✓ Design a personalized Harbor Ledger you’ll use for life

Through powerful stories, guided exercises, and easy-to-follow frameworks, this book gives you the tools to build a relationship that feels safe, supportive, passionate, and strong—no matter your past or personality differences.

Whether you're dating, engaged, newly married, or rebuilding after pain, this workbook will help you and your partner create a relationship that doesn’t just survive…
It thrives.

If you want clarity, connection, and a love that lasts—this is your blueprint.

Target Market(s)

couples

Font styles to use
Other font styles liked:
• a font used in making blueprints maybe a Leroy font

Colors
0054AA
0677BA
7BADD7
CADEEF
E8F1F8

Requirements
Must have
• a blueprint look
Nice to have
• eye catching 2 people

```html
<!DOCTYPE html>
<html lang="en">
<head>
<meta charset="utf-8">
<title>The Harbor Ledger – Book Cover Spread</title>
<link rel="stylesheet" href="https://fonts.googleapis.com/css2?family=Inter:wght@400;600;700&family=Saira+Condensed:wght@600;700&family=Roboto:ital,wght@1,700&display=swap">
<style>
  :root {
    --page-bg: #dcdcdc;
    --cover-blue: #2b4d79;
    --cover-blue-light: #4a6a92;
    --grid-line: rgba(123, 173, 215, 0.16);
    --ink: #e3eaf2;
    --ink-soft: #cadeef;
    --barcode-white: #f2f2f2;
  }
  * { box-sizing: border-box; margin: 0; padding: 0; }
  html, body { width: 1200px; height: 800px; overflow: hidden; }
  body {
    background: var(--page-bg);
    display: flex; align-items: center; justify-content: center;
    font-family: "Inter", sans-serif;
    color: var(--ink);
  }
  .cover-spread {
    display: flex;
    width: 1000px; height: 700px;
    background-color: var(--cover-blue);
    background-image:
      linear-gradient(var(--grid-line) 2px, transparent 2px),
      linear-gradient(90deg, var(--grid-line) 2px, transparent 2px);
    background-size: 34px 34px;
    box-shadow: 0 10px 30px rgba(0,0,0,0.25);
  }
  .back-cover {
    position: relative;
    width: 470px; height: 100%;
    padding: 38px 30px 30px 34px;
    font-size: 12.2px; line-height: 1.32; letter-spacing: 0.04em;
  }
  .back-hook { font-weight: 700; font-size: 13.5px; text-align: center; margin-bottom: 6px; }
  .back-cover p { margin-bottom: 12px; }
  .back-list-heading { font-weight: 700; font-size: 13px; margin-bottom: 4px; }
  .benefit-list { list-style: none; margin-bottom: 14px; }
  .benefit-list li { display: flex; gap: 4px; }
  .benefit-list svg { flex: none; margin-top: 3px; }
  .back-closing { font-weight: 700; font-size: 13px; }
  .barcode-space {
    position: absolute; right: 28px; bottom: 28px;
    width: 150px; height: 100px; background: var(--barcode-white);
  }
  .spine {
    width: 60px; height: 100%;
    display: flex; flex-direction: column; align-items: center; justify-content: space-between;
    padding: 30px 0;
    border-left: 1px solid rgba(255,255,255,0.08);
    border-right: 1px solid rgba(255,255,255,0.08);
  }
  .spine-text {
    writing-mode: vertical-rl;
    font-family: "Inter", sans-serif;
    color: var(--ink);
  }
  .spine-title { font-size: 17px; letter-spacing: 0.1em; }
  .spine-author { font-size: 22px; letter-spacing: 0.06em; }
  .front-cover {
    position: relative;
    width: 470px; height: 100%;
    background: radial-gradient(ellipse at 75% 55%, rgba(255,255,255,0.14), transparent 60%);
    text-align: center;
    padding-top: 48px;
  }
  .front-title {
    font-family: "Saira Condensed", sans-serif;
    font-weight: 700; line-height: 0.95;
    color: var(--ink-soft);
  }
  .front-title .title-lead { display: block; font-size: 44px; }
  .front-title .title-main { display: block; font-size: 78px; letter-spacing: 0.02em; }
  .front-subtitle {
    margin-top: 14px;
    font-family: "Roboto", sans-serif; font-style: italic; font-weight: 700;
    font-size: 18px; line-height: 1.35; color: var(--ink-soft);
  }
  .couple-illustration {
    position: absolute; left: 70px; top: 330px;
    width: 300px; height: 360px;
    background: linear-gradient(160deg, rgba(202,222,239,0.22), rgba(202,222,239,0.05));
    border-radius: 140px 140px 10px 10px;
  }
  .front-author {
    position: absolute; left: 0; right: 0; bottom: 28px;
    font-family: "Inter", sans-serif; font-weight: 600;
    font-size: 60px; letter-spacing: 0.01em; color: var(--ink-soft);
  }
</style>
</head>
<body>
  <main class="cover-spread">
    <section class="back-cover">
      <p class="back-hook">What if the strength of your relationship<br>came down to one thing—clarity?</p>
      <p>Most couples love each other deeply… but still misunderstand each other.<br>Not because they’re incompatible—because they never built a shared blueprint.</p>
      <p>The Harbor Ledger is a transformative relationship workbook designed to help couples replace confusion with clarity, resentment with understanding, and disconnection with deep, lasting partnership.</p>
      <p class="back-list-heading">Inside, you’ll learn how to:</p>
      <ul class="benefit-list">
        <li><svg width="10" height="10" viewBox="0 0 10 10"><path d="M1 5l3 3 5-7" fill="none" stroke="currentColor" stroke-width="1.4"/></svg><span>Communicate in ways that build connection—not conflict</span></li>
        <li><svg width="10" height="10" viewBox="0 0 10 10"><path d="M1 5l3 3 5-7" fill="none" stroke="currentColor" stroke-width="1.4"/></svg><span>Understand each other’s emotional needs, stress responses, and love patterns.</span></li>
        <li><svg width="10" height="10" viewBox="0 0 10 10"><path d="M1 5l3 3 5-7" fill="none" stroke="currentColor" stroke-width="1.4"/></svg><span>Set healthy boundaries without creating distance.</span></li>
        <li><svg width="10" height="10" viewBox="0 0 10 10"><path d="M1 5l3 3 5-7" fill="none" stroke="currentColor" stroke-width="1.4"/></svg><span>Rebuild trust and strengthen loyalty.</span></li>
        <li><svg width="10" height="10" viewBox="0 0 10 10"><path d="M1 5l3 3 5-7" fill="none" stroke="currentColor" stroke-width="1.4"/></svg><span>Navigate gender differences with empathy and confidence.</span></li>
        <li><svg width="10" height="10" viewBox="0 0 10 10"><path d="M1 5l3 3 5-7" fill="none" stroke="currentColor" stroke-width="1.4"/></svg><span>Balance intimacy, time, roles, finances, and expectations.</span></li>
        <li><svg width="10" height="10" viewBox="0 0 10 10"><path d="M1 5l3 3 5-7" fill="none" stroke="currentColor" stroke-width="1.4"/></svg><span>Create agreements that eliminate guesswork and prevent future conflict.</span></li>
        <li><svg width="10" height="10" viewBox="0 0 10 10"><path d="M1 5l3 3 5-7" fill="none" stroke="currentColor" stroke-width="1.4"/></svg><span>Design a personalized Harbor Ledger you’ll use for life.</span></li>
      </ul>
      <p>Through powerful stories, guided exercises, and easy-to-follow frameworks, this book gives you the tools to build a relationship that feels safe, supportive, passionate, and strong—no matter your past or personality differences.</p>
      <p>Whether you’re dating, engaged, newly married, or rebuilding after pain, this workbook will help you and your partner create a relationship that doesn’t just survive…It thrives.</p>
      <p class="back-closing">If you want clarity, connection,<br>and a love that lasts—<br>this is your blueprint.</p>
      <div class="barcode-space"></div>
    </section>

    <section class="spine">
      <span class="spine-text spine-title">THE HARBOR LEDGER</span>
      <span class="spine-text spine-author">Dorian Vell</span>
    </section>

    <section class="front-cover">
      <h1 class="front-title">
        <span class="title-lead">THE</span>
        <span class="title-main">HARBOR</span>
        <span class="title-main">LEDGER</span>
      </h1>
      <p class="front-subtitle">A Relationship Workbook to Strengthen<br>Clarity, Connection &amp; Lasting Love</p>
      <div class="couple-illustration" role="img" aria-label="White line-drawing outline of a couple embracing, in blueprint style"></div>
      <p class="front-author">Dorian Vell</p>
    </section>
  </main>
</body>
</html>
```